Page Template for Quillfern Supply

We are Quillfern Supply, a UK based reseller of Computer Memory, Equipment, Peripherals, Software and Services with a particular focus on Memory and Storage to businesses.

Our succesful ecommerce site at http://www.quillfern-supply.co.uk is now due a refresh. We are looking for a designer to produce a quality page template we can use throughout the site.

We will be using code from our corporate buying system http://k7.qfsupply.me.uk/ and a test version of the system is online at http://test.quillfernsupply.co.uk

We are keen for a "full-width" design - ie one that will stretch with the width of the user's monitor with a minimum width of 950px. It's also important that we can maintain our standards compliance. We are concerned with the colour scheme and layout of the page and the look of the buttons, bars, menus and peripheral elements etc. rather than any content. Please bear in mind that we are a British company and the layout must reflect design trends here rather than in the USA.

Layout should be suitable for product pages (eg. http://k7.qfsupply.me.uk/k7/product.php?id=5830914 ), memory pages (eg. http://k7.qfsupply.me.uk/k7/showMachine.php?machineid=602915 / http://www.brindlepart.co.uk/showMachine.php?machineid=602915 / http://www.quillfern-supply.co.uk/M-Veltrix-Orbdesk (mid+2010)-3.06GHz+Zenn+v3 21.5in-.html ) and content pages (eg http://www.quillfern-supply.co.uk/index.aspx?pageid=5 )

Might also be worth having a look at our other site at www.brindlepart.co.uk

Competitors' sites worth looking at:

www.harlowbyte.co.uk
www.tiwk.com
www.gradelinktrade.co.uk
www.foraxel.co.uk
www.sirplinth.co.uk

Reason: We're getting some great ideas through but we're well aware that quite a few designers are still at work either designing or perfecting designs. We're confident that with another few days of work, we'll be able to make an award.

Good morning, Designers,

Time is running out to participate in this contest, but there is still your opportunity to submit a design and walk away with the prize. Please remember the prize is in £ not $ - £225 is $370 US.

We've had some fantastic designs already, but it is still more than possible that a new designer could win. It is also our intention to award the participation payments to the designers who have put in the most effort, so it's well worth getting on board.

If you have questions please don't hesitate to send us a message.

Best regards,

Quillfern Supply

Target Market(s)

Business IT buyers in corporates and government departments

Industry/Entity Type

Computer

Requirements
Must have
• Must include:
a) large page content area
b) logo in top left
c) search box
d) QuickPeg code box
e) Shopping cart
f) full category menu per http://k7.qfsupply.me.uk
Should not have
• DO NOT ALTER OUR LOGO! This is non negotiable. Please also do not change the key corporate colour of #333399

```html
<!DOCTYPE html>
<html lang="en">
<head>
<meta charset="utf-8">
<title>Quillfern Supply – Page Template</title>
<link rel="stylesheet" href="https://fonts.googleapis.com/css2?family=Arimo:wght@400;700&family=PT+Sans:wght@400;700&display=swap">
<style>
:root{
  --brand:#333399;
  --brand-light:#5a58d0;
  --ink:#222222;
  --text:#555555;
  --muted:#777777;
  --line:#d4d4d4;
  --paper:#ffffff;
  --soft:#f1f1f1;
}
*{box-sizing:border-box;margin:0;padding:0}
html,body{width:1200px;height:909px;overflow:hidden;background:var(--paper)}
body{position:relative;font-family:Arimo,Arial,sans-serif;color:var(--ink)}
.abs{position:absolute}

/* header */
.brand{left:130px;top:40px;width:126px;height:116px}
.brand-mark{display:flex;align-items:center;gap:6px;margin-top:22px}
.brand-square{width:14px;height:14px;background:var(--brand)}
.brand-name{font-family:"PT Sans",sans-serif;font-weight:700;font-size:17px;color:var(--brand);line-height:1.1}
.brand-phone{font-family:"PT Sans",sans-serif;font-weight:700;font-size:17px;color:var(--brand);margin-top:34px;letter-spacing:.5px}
.account-links{right:131px;top:66px;font-size:12px;color:var(--muted)}
.account-links span{margin:0 7px}
.cart{right:131px;top:90px;display:flex;align-items:center;gap:6px;font-size:12px;color:var(--muted)}
.prefs{right:131px;top:128px;display:flex;align-items:center;font-size:11px;color:var(--muted)}
.select{width:92px;height:22px;border:1px solid #ccc;border-radius:3px;margin-left:20px;margin-right:15px;display:flex;align-items:center;justify-content:space-between;padding-left:9px;font-size:11px;color:#888;background:#fff;overflow:hidden}
.select:last-child{margin-right:0;margin-left:8px}
.select i{width:22px;height:22px;background:linear-gradient(#5c5ac9,var(--brand));display:flex;align-items:center;justify-content:center}

/* navigation */
.nav{left:130px;top:159px;width:940px;height:51px;border:1px solid #ccc;border-radius:4px;background:linear-gradient(#ffffff,#f0f0f0)}
.nav-item{top:17px;font-size:12.5px;color:var(--ink)}
.nav-sep{top:8px;width:1px;height:34px;background:#ddd}
.search-input{left:744px;top:13px;width:144px;height:23px;border:1px solid #bbb;background:#fff}
.search-btn{left:896px;top:12px;width:28px;height:24px;border-radius:3px;background:linear-gradient(#6a68dc,var(--brand));display:flex;align-items:center;justify-content:center}

/* hero */
.hero{left:130px;top:220px;width:940px;height:326px;border:1px solid #ddd;border-radius:4px}
.offer{left:6px;width:249px;height:62px;background:linear-gradient(#ffffff,#e6e6e6);border-bottom:1px solid #fff;display:flex;align-items:center;gap:10px;padding-left:20px;font-family:"PT Sans",sans-serif;font-size:19px;letter-spacing:-.4px;color:#333}
.offer.is-active{background:var(--brand);color:#fff}
.offer-dot{width:23px;height:23px;border-radius:50%;background:linear-gradient(#fff,#d9d9d9);box-shadow:0 1px 2px rgba(0,0,0,.25);display:flex;align-items:center;justify-content:center}
.banner{left:255px;top:7px;width:676px;height:310px;background:radial-gradient(ellipse at 65% 10%,#7d7bf2 0%,#5552d6 45%,#3b37ad 100%)}
.banner-kicker{left:60px;top:99px;font-family:"PT Sans",sans-serif;font-size:19px;letter-spacing:-.5px;color:#fff}
.banner-title{left:59px;top:134px;font-family:"PT Sans",sans-serif;font-size:31px;letter-spacing:-1px;color:#fff;line-height:1.05}
.banner-title b{font-weight:400;font-size:41px;letter-spacing:-.5px;display:block}
.banner-visual{left:430px;top:10px;width:220px;height:286px;border-radius:10px;background:linear-gradient(160deg,#e6ecf2 0%,#9fb4c8 40%,#4e8fd0 60%,#c9d3dc 100%);opacity:.9}

/* spotlight */
.section-title{font-family:"PT Sans",sans-serif;font-size:23px;color:#333}
.section-title em{font-style:normal;color:var(--brand)}
.spot-arrow{top:636px}
.spot-img{top:610px;width:102px;height:76px;border-radius:4px}
.spot-name{top:619px;font-size:13px;font-weight:700;color:#000;line-height:20px;width:110px}
.spot-deal{top:659px;font-size:13px;font-weight:700;color:var(--brand)}

/* categories */
.cat-head{left:137px;top:719px;width:243px;height:31px;border:1px solid #ddd;border-radius:2px;background:linear-gradient(#fff,#eee);padding:5px 0 0 17px;font-size:16px;color:#333}
.cat-list{left:137px;top:761px;width:243px;list-style:none}
.cat-list li{height:30px;border-bottom:1px dotted #ccc;font-size:14px;color:var(--text);padding:7px 0 0 31px;position:relative}
.cat-list li::before{content:"";position:absolute;left:19px;top:13px;border-left:4px solid var(--brand);border-top:3px solid transparent;border-bottom:3px solid transparent}

/* featured */
.view-all{left:908px;top:724px;width:142px;height:23px;border-radius:3px;background:linear-gradient(#6866d8,var(--brand));color:#fff;font-size:13px;font-weight:700;text-align:center;line-height:23px}
.prod-sep{top:768px;width:0;height:141px;border-left:1px dotted #ccc}
.prod-img{top:778px;width:120px;height:102px;border-radius:6px}
.prod-name{top:902px;font-size:12px;color:#222}
</style>
</head>
<body>

<!-- header -->
<div class="abs brand">
  <div class="brand-mark"><span class="brand-square"></span><span class="brand-name">Quillfern Supply</span></div>
  <div class="brand-phone">020 7946 0321</div>
</div>

<div class="abs account-links">Login<span>|</span>Register for Business Account and Discounts<span>|</span>Request quotation</div>

<div class="abs cart">
  <svg width="28" height="26" viewBox="0 0 28 26" aria-hidden="true">
    <path d="M5 7h3l3 11h11l3-8H10" fill="none" stroke="#444" stroke-width="2"/>
    <circle cx="12" cy="22" r="2" fill="#444"/><circle cx="21" cy="22" r="2" fill="#444"/>
    <circle cx="7" cy="6" r="5" fill="#4caf1f"/><path d="M7 3v6M4 6h6" stroke="#fff" stroke-width="1.6"/>
  </svg>
  Shopping cart is empty
</div>

<div class="abs prefs">
  Language:
  <div class="select">English<i><svg width="9" height="6"><path d="M0 0h9L4.5 6z" fill="#fff"/></svg></i></div>
  Currencies:
  <div class="select">GBP<i><svg width="9" height="6"><path d="M0 0h9L4.5 6z" fill="#fff"/></svg></i></div>
</div>

<!-- navigation -->
<nav class="abs nav">
  <span class="abs nav-item" style="left:18px">Memory</span><span class="abs nav-sep" style="left:76px"></span>
  <span class="abs nav-item" style="left:94px">Audio Visual</span><span class="abs nav-sep" style="left:176px"></span>
  <span class="abs nav-item" style="left:195px">Printers</span><span class="abs nav-sep" style="left:253px"></span>
  <span class="abs nav-item" style="left:271px">PC &amp; Laptops</span><span class="abs nav-sep" style="left:363px"></span>
  <span class="abs nav-item" style="left:380px">Networking</span><span class="abs nav-sep" style="left:457px"></span>
  <span class="abs nav-item" style="left:475px">Components</span><span class="abs nav-sep" style="left:563px"></span>
  <span class="abs nav-item" style="left:580px">Storage</span><span class="abs nav-sep" style="left:640px"></span>
  <span class="abs nav-item" style="left:656px">Software</span><span class="abs nav-sep" style="left:719px"></span>
  <div class="abs search-input"></div>
  <div class="abs search-btn"><svg width="16" height="16" viewBox="0 0 16 16" aria-hidden="true"><circle cx="6.5" cy="6.5" r="4.5" fill="none" stroke="#fff" stroke-width="2"/><path d="M10 10l4.5 4.5" stroke="#fff" stroke-width="2.4"/></svg></div>
</nav>

<!-- hero -->
<section class="abs hero">
  <div class="abs offer" style="top:7px"><span class="offer-dot"><svg width="7" height="9"><path d="M1 1l4 3.5L1 8" fill="none" stroke="#4a48c4" stroke-width="1.6"/></svg></span>50% Discount Insanity</div>
  <div class="abs offer is-active" style="top:69px"><span class="offer-dot"><svg width="7" height="9"><path d="M1 1l4 3.5L1 8" fill="none" stroke="#4a48c4" stroke-width="1.6"/></svg></span>Premium Products</div>
  <div class="abs offer" style="top:131px"><span class="offer-dot"><svg width="7" height="9"><path d="M1 1l4 3.5L1 8" fill="none" stroke="#4a48c4" stroke-width="1.6"/></svg></span>Exclusive Offer</div>
  <div class="abs offer" style="top:193px"><span class="offer-dot"><svg width="7" height="9"><path d="M1 1l4 3.5L1 8" fill="none" stroke="#4a48c4" stroke-width="1.6"/></svg></span>Red Hot Stuff</div>
  <div class="abs offer" style="top:255px;height:62px"><span class="offer-dot"><svg width="7" height="9"><path d="M1 1l4 3.5L1 8" fill="none" stroke="#4a48c4" stroke-width="1.6"/></svg></span>Summertime Discount</div>

  <div class="abs banner">
    <div class="abs banner-kicker">Nice chance to get what you want!</div>
    <div class="abs banner-title">Discounts for new items<b>are active!</b></div>
    <div class="abs banner-visual" role="img" aria-label="Silver widescreen monitor with a glowing blue circuit display"></div>
  </div>
</section>

<!-- spotlight -->
<h2 class="abs section-title" style="left:155px;top:563px;font-weight:400">Our <em>Spotlight</em></h2>

<svg class="abs spot-arrow" style="left:130px" width="13" height="22" aria-hidden="true"><path d="M12 0L0 11l12 11z" fill="var(--brand)"/></svg>
<svg class="abs spot-arrow" style="left:1058px" width="13" height="22" aria-hidden="true"><path d="M0 0l12 11L0 22z" fill="var(--brand)"/></svg>

<div class="abs spot-img" style="left:170px;background:linear-gradient(#e4e4e4,#3a3a3a)" role="img" aria-label="Black handheld camcorder"></div>
<div class="abs spot-name" style="left:285px">Camcorders</div>
<div class="abs spot-deal" style="left:285px">Save £ 40 ›</div>

<div class="abs spot-img" style="left:400px;background:linear-gradient(#9a3540,#2a2a2a)" role="img" aria-label="Red notebook PC"></div>
<div class="abs spot-name" style="left:516px">Notebook PC</div>
<div class="abs spot-deal" style="left:516px">Save £ 55 ›</div>

<div class="abs spot-img" style="left:632px;background:linear-gradient(#f2f2f2,#7a7a7a)" role="img" aria-label="Inkjet office printer with printed pages"></div>
<div class="abs spot-name" style="left:747px">Norvane JetPrint K210 Printer</div>
<div class="abs spot-deal" style="left:747px">Free Shipping ›</div>

<div class="abs spot-img" style="left:872px;width:74px;background:linear-gradient(#5b9a3c,#1a1a1a)" role="img" aria-label="Widescreen monitor showing a landscape"></div>
<div class="abs spot-name" style="left:958px;width:80px">KELDRA 2243KX</div>
<div class="abs spot-deal" style="left:958px">Save £ 24 ›</div>

<!-- categories -->
<div class="abs cat-head">Categories</div>
<ul class="abs cat-list">
  <li>Memory</li><li>AV</li><li>Cables</li><li>Components</li><li>Computing</li>
</ul>

<!-- featured -->
<h2 class="abs section-title" style="left:426px;top:719px;font-weight:400">Featured <em>Products</em></h2>
<div class="abs view-all">View All Products</div>

<span class="abs prod-sep" style="left:575px"></span>
<span class="abs prod-sep" style="left:739px"></span>
<span class="abs prod-sep" style="left:903px"></span>

<div class="abs prod-img" style="left:432px;background:linear-gradient(#5a5a5a,#1e1e1e)" role="img" aria-label="Touchscreen smartphone"></div>
<div class="abs prod-img" style="left:598px;background:linear-gradient(#3fa0c8,#1a1a1a)" role="img" aria-label="Widescreen computer monitor"></div>
<div class="abs prod-img" style="left:758px;background:linear-gradient(#d8d8d8,#222)" role="img" aria-label="Home theatre speaker system"></div>
<div class="abs prod-img" style="left:922px;background:linear-gradient(#6a6a6a,#111)" role="img" aria-label="Black home projector"></div>

<div class="abs prod-name" style="left:426px">Norvane Nexa Phone</div>
<div class="abs prod-name" style="left:598px">Keldra 2243KX</div>
<div class="abs prod-name" style="left:762px">Home Theatre</div>
<div class="abs prod-name" style="left:926px">Home Projector</div>

</body>
</html>
```